Web Page Re-designed

Looking to have this portion of a webpage on my site re-designed to look a little more clean and professional, the layout and organization of the data can be changed for example the location name does not have to keep repeating itself its schedule for a sports league

Reason: Still looking fo the right design

It Professional

```html
<!DOCTYPE html>
<html lang="en">
<head>
<meta charset="utf-8">
<title>Wednesday Co-ed Ball Hockey Schedule</title>
<link href="https://fonts.googleapis.com/css2?family=Roboto:ital,wght@0,400;0,500;0,700;1,700&display=swap" rel="stylesheet">
<style>
:root{
  --green:#76b139;
  --dark:#333333;
  --white:#ffffff;
  --cell:#f7f7f7;
  --select:#ebebeb;
  --text:#333333;
  --muted:#666666;
  --rule:#dddddd;
  --orange:#f7941d;
  --yellow:#f5f21b;
}
*{box-sizing:border-box;margin:0;padding:0}
html,body{width:1200px;height:958px;overflow:hidden}
body{background:var(--green);font-family:'Roboto',sans-serif;color:var(--text)}
.page{position:absolute;left:112px;top:0;width:979px;height:958px;background:var(--white)}
.topbar{position:absolute;left:13px;top:13px;width:953px;height:54px;background:var(--dark);display:flex;align-items:center;padding-left:6px}
.topbar svg{margin-right:11px}
.title{color:var(--white);font-weight:700;font-size:24px;letter-spacing:-.2px}
.title em{font-size:14px;font-style:italic;margin-left:4px;letter-spacing:.2px}
.select{position:absolute;display:flex;height:38px}
.select .label{flex:1;display:flex;align-items:center;padding-left:13px;font-size:12px;font-weight:500;color:var(--muted)}
.select .btn{width:38px;background:var(--green);display:flex;align-items:center;justify-content:center}
.season{left:716px;top:9px;width:241px}
.season .label{background:var(--white)}
.team{left:226px;top:78px;width:241px}
.team .label,.type .label{background:var(--select)}
.type{left:721px;top:78px;width:241px}
.sidebar{position:absolute;left:13px;top:78px;width:194px}
.side-head{height:38px;background:var(--dark);color:var(--white);display:flex;align-items:center;padding-left:9px;font-size:16px;font-weight:500}
.side-head svg{margin-right:13px}
.side-list{list-style:none;margin-bottom:24px}
.side-list li{height:41px;display:flex;align-items:center;padding-left:14px;font-size:14px;border-bottom:1px solid var(--rule)}
.side-list li:last-child{border-bottom:none}
.main{position:absolute;left:226px;top:129px;width:735px}
.day{margin-bottom:14px}
.day-head{height:39px;background:var(--dark);color:var(--white);display:flex;align-items:center;padding-left:8px;font-size:16px;font-weight:500}
.day-head svg{margin-right:12px}
.games{border-collapse:separate;border-spacing:2px 2px;margin:1px -2px 0;width:739px}
.games td,.games th{background:var(--cell);height:50px;text-align:center;font-size:14px;font-weight:400}
.games th{color:var(--green);font-size:14px;font-weight:400}
.games .sticks{font-size:12px}
.games th.sticks{font-size:14px}
.games .loc{text-decoration:underline;text-underline-offset:3px}
.games .vs{font-size:13px}
</style>
</head>
<body>
<div class="page">
  <header class="topbar">
    <svg width="30" height="30" viewBox="0 0 30 30"><rect x="1" y="4" width="28" height="25" rx="2" fill="#fff"/><rect x="3" y="10" width="24" height="17" fill="#333"/><rect x="7" y="1" width="3" height="6" fill="#fff"/><rect x="20" y="1" width="3" height="6" fill="#fff"/><g fill="#fff"><rect x="6" y="13" width="3" height="3"/><rect x="11" y="13" width="3" height="3"/><rect x="16" y="13" width="3" height="3"/><rect x="21" y="13" width="3" height="3"/><rect x="6" y="18" width="3" height="3"/><rect x="11" y="18" width="3" height="3"/><rect x="16" y="18" width="3" height="3"/><rect x="21" y="18" width="3" height="3"/><rect x="6" y="22" width="3" height="3"/><rect x="11" y="22" width="3" height="3"/><rect x="16" y="22" width="3" height="3"/></g></svg>
    <h1 class="title">WEDNESDAY<em>CO-ED BALL HOCKEY SCHEDULE</em></h1>
    <div class="select season"><span class="label">FALL 2013</span><span class="btn"><svg width="10" height="6"><path d="M0 0h10L5 6z" fill="#fff"/></svg></span></div>
  </header>

  <div class="select team"><span class="label">CHOOSE TEAM</span><span class="btn"><svg width="10" height="6"><path d="M0 0h10L5 6z" fill="#fff"/></svg></span></div>
  <div class="select type"><span class="label">REGULAR SEASON/EXHIBITION</span><span class="btn"><svg width="10" height="6"><path d="M0 0h10L5 6z" fill="#fff"/></svg></span></div>

  <nav class="sidebar">
    <div class="side-head"><svg width="24" height="24" viewBox="0 0 24 24"><rect x="1" y="3" width="22" height="20" rx="2" fill="none" stroke="#fff" stroke-width="2"/><rect x="5" y="0" width="2" height="5" fill="#fff"/><rect x="17" y="0" width="2" height="5" fill="#fff"/><g fill="#fff"><rect x="6" y="10" width="2" height="2"/><rect x="11" y="10" width="2" height="2"/><rect x="16" y="10" width="2" height="2"/><rect x="6" y="14" width="2" height="2"/><rect x="11" y="14" width="2" height="2"/><rect x="16" y="14" width="2" height="2"/><rect x="11" y="18" width="2" height="2"/></g></svg>Schedules</div>
    <ul class="side-list"><li>Division A</li><li>Division B</li><li>Division C</li></ul>
    <div class="side-head"><svg width="24" height="24" viewBox="0 0 24 24" fill="none" stroke="#fff" stroke-width="3" stroke-linecap="round"><path d="M10 14l4-4"/><path d="M11 6l2-2a4 4 0 016 6l-2 2"/><path d="M13 18l-2 2a4 4 0 01-6-6l2-2"/></svg>Links</div>
    <ul class="side-list"><li>Rules</li><li>Teams</li><li>News</li><li>Free Agents</li><li>Champ T-Shirt Request</li></ul>
    <div class="side-head"><svg width="24" height="24" viewBox="0 0 24 24" fill="none" stroke="#fff" stroke-width="2"><path d="M1 17l7-7 5 5 5-6 5 5"/></svg>Stats</div>
    <ul class="side-list"><li>Game Results</li><li>Scoreboard</li><li>Standings</li><li>Leaders</li></ul>
  </nav>

  <main class="main">
    <section class="day">
      <h2 class="day-head"><svg width="24" height="24" viewBox="0 0 24 24"><rect x="1" y="3" width="22" height="20" rx="2" fill="none" stroke="#fff" stroke-width="2"/><rect x="5" y="0" width="2" height="5" fill="#fff"/><rect x="17" y="0" width="2" height="5" fill="#fff"/><g fill="#fff"><rect x="6" y="10" width="2" height="2"/><rect x="11" y="10" width="2" height="2"/><rect x="16" y="10" width="2" height="2"/><rect x="6" y="14" width="2" height="2"/><rect x="11" y="14" width="2" height="2"/><rect x="16" y="14" width="2" height="2"/><rect x="11" y="18" width="2" height="2"/></g></svg>Wednesday,&nbsp; Oct 2nd</h2>
      <table class="games">
        <colgroup><col style="width:38px"><col style="width:81px"><col style="width:130px"><col style="width:50px"><col style="width:50px"><col style="width:131px"><col style="width:49px"><col style="width:130px"><col style="width:60px"></colgroup>
        <tr><th></th><th>TIME</th><th>HOME</th><th></th><th></th><th>AWAY</th><th></th><th>LOCATION</th><th class="sticks">STICKS</th></tr>
        <tr><td>RS</td><td>8:00pm</td><td>BLUE LINERS</td><td><svg width="28" height="20" viewBox="0 0 28 20"><path d="M9 1h10l8 4-3 6-3-2v10H7V9l-3 2-3-6z" fill="var(--orange)" stroke="#555" stroke-width=".8"/></svg></td><td class="vs">vs.</td><td>Pass Masters</td><td><svg width="28" height="20" viewBox="0 0 28 20"><path d="M9 1h10l8 4-3 6-3-2v10H7V9l-3 2-3-6z" fill="var(--yellow)" stroke="#555" stroke-width=".8"/></svg></td><td class="loc">Northgate Arena</td><td class="sticks">No Wood</td></tr>
        <tr><td>RS</td><td>8:00pm</td><td>BLUE LINERS</td><td><svg width="28" height="20" viewBox="0 0 28 20"><path d="M9 1h10l8 4-3 6-3-2v10H7V9l-3 2-3-6z" fill="var(--orange)" stroke="#555" stroke-width=".8"/></svg></td><td class="vs">vs.</td><td>Pass Masters</td><td><svg width="28" height="20" viewBox="0 0 28 20"><path d="M9 1h10l8 4-3 6-3-2v10H7V9l-3 2-3-6z" fill="var(--yellow)" stroke="#555" stroke-width=".8"/></svg></td><td class="loc">Northgate Arena</td><td class="sticks">No Wood</td></tr>
        <tr><td>RS</td><td>8:00pm</td><td>BLUE LINERS</td><td><svg width="28" height="20" viewBox="0 0 28 20"><path d="M9 1h10l8 4-3 6-3-2v10H7V9l-3 2-3-6z" fill="var(--orange)" stroke="#555" stroke-width=".8"/></svg></td><td class="vs">vs.</td><td>Pass Masters</td><td><svg width="28" height="20" viewBox="0 0 28 20"><path d="M9 1h10l8 4-3 6-3-2v10H7V9l-3 2-3-6z" fill="var(--yellow)" stroke="#555" stroke-width=".8"/></svg></td><td class="loc">Northgate Arena</td><td class="sticks">No Wood</td></tr>
      </table>
    </section>

    <section class="day">
      <h2 class="day-head"><svg width="24" height="24" viewBox="0 0 24 24"><rect x="1" y="3" width="22" height="20" rx="2" fill="none" stroke="#fff" stroke-width="2"/><rect x="5" y="0" width="2" height="5" fill="#fff"/><rect x="17" y="0" width="2" height="5" fill="#fff"/><g fill="#fff"><rect x="6" y="10" width="2" height="2"/><rect x="11" y="10" width="2" height="2"/><rect x="16" y="10" width="2" height="2"/><rect x="6" y="14" width="2" height="2"/><rect x="11" y="14" width="2" height="2"/><rect x="16" y="14" width="2" height="2"/><rect x="11" y="18" width="2" height="2"/></g></svg>Wednesday,&nbsp; Oct 9th</h2>
      <table class="games">
        <colgroup><col style="width:38px"><col style="width:81px"><col style="width:130px"><col style="width:50px"><col style="width:50px"><col style="width:131px"><col style="width:49px"><col style="width:130px"><col style="width:60px"></colgroup>
        <tr><th></th><th>TIME</th><th>HOME</th><th></th><th></th><th>AWAY</th><th></th><th>LOCATION</th><th class="sticks">STICKS</th></tr>
        <tr><td>RS</td><td>8:00pm</td><td>BLUE LINERS</td><td><svg width="28" height="20" viewBox="0 0 28 20"><path d="M9 1h10l8 4-3 6-3-2v10H7V9l-3 2-3-6z" fill="var(--orange)" stroke="#555" stroke-width=".8"/></svg></td><td class="vs">vs.</td><td>Pass Masters</td><td><svg width="28" height="20" viewBox="0 0 28 20"><path d="M9 1h10l8 4-3 6-3-2v10H7V9l-3 2-3-6z" fill="var(--yellow)" stroke="#555" stroke-width=".8"/></svg></td><td class="loc">Northgate Arena</td><td class="sticks">No Wood</td></tr>
        <tr><td>RS</td><td>8:00pm</td><td>BLUE LINERS</td><td><svg width="28" height="20" viewBox="0 0 28 20"><path d="M9 1h10l8 4-3 6-3-2v10H7V9l-3 2-3-6z" fill="var(--orange)" stroke="#555" stroke-width=".8"/></svg></td><td class="vs">vs.</td><td>Pass Masters</td><td><svg width="28" height="20" viewBox="0 0 28 20"><path d="M9 1h10l8 4-3 6-3-2v10H7V9l-3 2-3-6z" fill="var(--yellow)" stroke="#555" stroke-width=".8"/></svg></td><td class="loc">Northgate Arena</td><td class="sticks">No Wood</td></tr>
        <tr><td>RS</td><td>8:00pm</td><td>BLUE LINERS</td><td><svg width="28" height="20" viewBox="0 0 28 20"><path d="M9 1h10l8 4-3 6-3-2v10H7V9l-3 2-3-6z" fill="var(--orange)" stroke="#555" stroke-width=".8"/></svg></td><td class="vs">vs.</td><td>Pass Masters</td><td><svg width="28" height="20" viewBox="0 0 28 20"><path d="M9 1h10l8 4-3 6-3-2v10H7V9l-3 2-3-6z" fill="var(--yellow)" stroke="#555" stroke-width=".8"/></svg></td><td class="loc">Northgate Arena</td><td class="sticks">No Wood</td></tr>
      </table>
    </section>

    <section class="day">
      <h2 class="day-head"><svg width="24" height="24" viewBox="0 0 24 24"><rect x="1" y="3" width="22" height="20" rx="2" fill="none" stroke="#fff" stroke-width="2"/><rect x="5" y="0" width="2" height="5" fill="#fff"/><rect x="17" y="0" width="2" height="5" fill="#fff"/><g fill="#fff"><rect x="6" y="10" width="2" height="2"/><rect x="11" y="10" width="2" height="2"/><rect x="16" y="10" width="2" height="2"/><rect x="6" y="14" width="2" height="2"/><rect x="11" y="14" width="2" height="2"/><rect x="16" y="14" width="2" height="2"/><rect x="11" y="18" width="2" height="2"/></g></svg>Wednesday,&nbsp; Oct 16th</h2>
      <table class="games">
        <colgroup><col style="width:38px"><col style="width:81px"><col style="width:130px"><col style="width:50px"><col style="width:50px"><col style="width:131px"><col style="width:49px"><col style="width:130px"><col style="width:60px"></colgroup>
        <tr><th></th><th>TIME</th><th>HOME</th><th></th><th></th><th>AWAY</th><th></th><th>LOCATION</th><th class="sticks">STICKS</th></tr>
        <tr><td>RS</td><td>8:00pm</td><td>BLUE LINERS</td><td><svg width="28" height="20" viewBox="0 0 28 20"><path d="M9 1h10l8 4-3 6-3-2v10H7V9l-3 2-3-6z" fill="var(--orange)" stroke="#555" stroke-width=".8"/></svg></td><td class="vs">vs.</td><td>Pass Masters</td><td><svg width="28" height="20" viewBox="0 0 28 20"><path d="M9 1h10l8 4-3 6-3-2v10H7V9l-3 2-3-6z" fill="var(--yellow)" stroke="#555" stroke-width=".8"/></svg></td><td class="loc">Northgate Arena</td><td class="sticks">No Wood</td></tr>
        <tr><td>RS</td><td>8:00pm</td><td>BLUE LINERS</td><td><svg width="28" height="20" viewBox="0 0 28 20"><path d="M9 1h10l8 4-3 6-3-2v10H7V9l-3 2-3-6z" fill="var(--orange)" stroke="#555" stroke-width=".8"/></svg></td><td class="vs">vs.</td><td>Pass Masters</td><td><svg width="28" height="20" viewBox="0 0 28 20"><path d="M9 1h10l8 4-3 6-3-2v10H7V9l-3 2-3-6z" fill="var(--yellow)" stroke="#555" stroke-width=".8"/></svg></td><td class="loc">Northgate Arena</td><td class="sticks">No Wood</td></tr>
        <tr><td>RS</td><td>8:00pm</td><td>BLUE LINERS</td><td><svg width="28" height="20" viewBox="0 0 28 20"><path d="M9 1h10l8 4-3 6-3-2v10H7V9l-3 2-3-6z" fill="var(--orange)" stroke="#555" stroke-width=".8"/></svg></td><td class="vs">vs.</td><td>Pass Masters</td><td><svg width="28" height="20" viewBox="0 0 28 20"><path d="M9 1h10l8 4-3 6-3-2v10H7V9l-3 2-3-6z" fill="var(--yellow)" stroke="#555" stroke-width=".8"/></svg></td><td class="loc">Northgate Arena</td><td class="sticks">No Wood</td></tr>
      </table>
    </section>
  </main>
</div>
</body>
</html>
```